Hot Consulting firm collateral upgrade

We need a stationary design for our Oakland based consulting company called Travilux. We provide consulting expertise in KRB compliance for Medical Device, Pharmaceutical, and Biotech companies. We will be using the stationary for all of our marketing collateral. We want the design to convey professionalism and quality. You can find our company color scheme from our website travilux-example.com. I have included a copy of our current stationary that needs an upgrade.
Target Market(s)
Medical Device, Pharma, and Biotech companies
Industry/Entity Type
It Company
Look and feel

```html
<!DOCTYPE html>
<html lang="en">
<head>
<meta charset="utf-8">
<title>Travilux Business Card</title>
<link href="https://fonts.googleapis.com/css2?family=Mulish:wght@400;700&display=swap" rel="stylesheet">
<style>
  :root {
    --backdrop: #202022;
    --card-white: #f6f6f6;
    --brand-blue: #0d3f88;
    --brand-blue-deep: #0b3677;
    --text-grey: #4a4a4a;
    --white: #ffffff;
  }
  * { margin: 0; padding: 0; box-sizing: border-box; }
  html, body {
    width: 1200px; height: 1000px; overflow: hidden;
    background: var(--backdrop);
    font-family: "Mulish", "Century Gothic", sans-serif;
  }
  .canvas { position: relative; width: 1200px; height: 1000px; }

  .card {
    position: absolute; width: 578px; height: 322px;
    border-radius: 16px; overflow: hidden;
  }
  .card--front { left: 202px; top: 150px; background: var(--card-white); }
  .card--back {
    left: 420px; top: 548px;
    background: linear-gradient(160deg, #13489a 0%, var(--brand-blue-deep) 100%);
  }

  .front__band {
    position: absolute; left: 0; right: 0; bottom: 0; height: 20px;
    background: var(--brand-blue);
  }
  .front__address {
    position: absolute; left: 30px; top: 73px; font-style: normal;
    font-size: 13.5px; line-height: 18px; color: var(--text-grey);
  }
  .contact-list {
    position: absolute; left: 30px; top: 226px; list-style: none;
    font-size: 14px; line-height: 18px; color: var(--text-grey);
  }
  .contact-list li { display: flex; align-items: center; gap: 8px; }
  .contact-list svg { width: 14px; height: 14px; flex: none; }

  .wordmark {
    position: absolute; font-weight: 700; letter-spacing: 2px;
    line-height: 1; text-transform: uppercase;
  }
  .front .wordmark { right: 30px; top: 84px; font-size: 38px; color: var(--brand-blue); }
  .back .wordmark { right: 42px; top: 152px; font-size: 32px; color: var(--white); }

  .person { position: absolute; right: 30px; top: 222px; text-align: right; }
  .person__name {
    font-weight: 700; font-size: 20px; color: var(--brand-blue); letter-spacing: 0.3px;
  }
  .person__title { font-size: 15px; color: var(--text-grey); margin-top: 2px; }
</style>
</head>
<body>
<main class="canvas">
  <section class="card card--front front">
    <address class="front__address">
      Bay Area HQ<br>4120 Harbor Lane<br>Oakland, CA 94607
    </address>

    <p class="wordmark">Travilux</p>

    <ul class="contact-list">
      <li>
        <svg viewBox="0 0 14 14" aria-hidden="true"><rect width="14" height="14" rx="2" fill="#0d3f88"/><path d="M4 3.2c.5-.4 1-.3 1.3.2l.7 1.2c.2.4.1.8-.2 1l-.5.4c.4.9 1 1.6 1.9 2l.4-.5c.3-.3.7-.4 1-.2l1.2.7c.5.3.6.8.2 1.3l-.5.6c-.4.4-1 .5-1.6.3C6 9.5 4.6 8.1 3.8 6.2c-.2-.6-.1-1.2.3-1.6z" fill="#fff"/></svg>
        <span>(510) 555- 0142</span>
      </li>
      <li>
        <svg viewBox="0 0 14 14" aria-hidden="true"><rect width="14" height="14" rx="2" fill="#0d3f88"/><rect x="3" y="4.2" width="8" height="5.6" fill="none" stroke="#fff" stroke-width="1"/><path d="M3 4.4 7 7.4l4-3" fill="none" stroke="#fff" stroke-width="1"/></svg>
        <span>info@travilux-example.com</span>
      </li>
      <li>
        <svg viewBox="0 0 14 14" aria-hidden="true"><rect width="14" height="14" rx="2" fill="#0d3f88"/><g fill="none" stroke="#fff" stroke-width="0.9"><circle cx="7" cy="7" r="4"/><ellipse cx="7" cy="7" rx="1.7" ry="4"/><path d="M3 7h8"/></g></svg>
        <span>www.travilux-example.com</span>
      </li>
    </ul>

    <div class="person">
      <p class="person__name">JORDAN MERCER</p>
      <p class="person__title">Account Executive</p>
    </div>

    <div class="front__band"></div>
  </section>

  <section class="card card--back back">
    <p class="wordmark">Travilux</p>
  </section>
</main>
</body>
</html>
```